Business broker needs designs for business card, letterhead and email signature

I require the following items:
- business cards
- letterhead
- email signature

My company is a Business Broker company that specialises in business sales across various industries. The company has branches in four areas and each area has its own logo and website. Initially for the submission I am happy to inspect 1 design and 1 layout for tallowgatedeals but the winner will need to complete a design for each area.

The four areas are:
1. tallowgatedeals
2. pinecrestfuelagent
3. harrowlinkagent
4. bramblegroceragent

I would like one design for each of the above items for each area. In each design, there should be one prominent logo and then the remaining three should also be included, for eg, the letterhead for the tallowgatedeal area would have the tallowgatedeal logo featuring prominently, somewhere at the top perhaps and the logos of the other three areas would be smaller and perhaps at the bottom, down the side, etc.

For the business cards, one prominent logo should feature on one side with the remaining three logos on the reverse.

The overall objective is for each item to look like it belongs to one family . I need all the source files as I may add new industries moving forward.

Target Market(s)

My company targets business minded people looking to increase wealth,. make an investment or migrate to Australia. People who busy and are looking for efficient and professional service in securing their next business venture.

Industry/Entity Type

Business

Font styles to use
Serif
Sans Serif

Requirements
Must have
• I want something professional and corporate looking, not something cartoony or playful. I am happy for you to be creative.

```html
<!DOCTYPE html>
<html lang="en">
<head>
<meta charset="utf-8">
<title>tallowgatedeals — business card</title>
<link rel="stylesheet" href="https://fonts.googleapis.com/css2?family=Source+Sans+3:ital,wght@0,400;0,600;0,700;1,700&display=swap">
<style>
  :root {
    --brand-red: #d3123f;
    --brand-slate: #46525b;
    --ink: #111111;
    --paper: #ffffff;
    --backdrop: #d5d7d8;
  }
  * { box-sizing: border-box; margin: 0; padding: 0; }
  html, body {
    width: 1200px; height: 854px; overflow: hidden;
    background: var(--backdrop);
    font-family: "Source Sans 3", Arial, sans-serif;
  }
  .stage {
    position: relative; width: 1200px; height: 854px;
  }
  .card {
    position: absolute; left: 290px;
    width: 620px; height: 378px;
    background: var(--paper);
    box-shadow: 0 6px 18px rgba(0,0,0,0.12);
    overflow: hidden;
  }
  .card--front { top: 29px; }
  .card--back { top: 447px; }

  /* front */
  .accent-bar {
    position: absolute; left: 0; top: 96px;
    width: 9px; height: 256px; background: var(--brand-red);
  }
  .holder-name {
    position: absolute; left: 32px; top: 94px;
    font-size: 27px; font-weight: 700; font-style: italic; color: var(--brand-red);
  }
  .holder-title {
    position: absolute; left: 32px; top: 132px;
    font-size: 20px; color: var(--ink);
  }
  .contact {
    position: absolute; left: 32px; top: 246px;
    list-style: none; font-size: 20px; line-height: 27px;
  }
  .contact__item { color: var(--brand-red); }
  .contact__item--address { color: var(--ink); }
  .front-mark {
    position: absolute; left: 408px; top: 30px;
    width: 176px; text-align: center;
  }
  .front-mark__circle {
    display: block; width: 150px; height: 150px; margin: 0 auto;
    border-radius: 50%; background: var(--brand-slate);
  }
  .front-mark__name {
    display: block; margin-top: 10px;
    font-size: 19px; font-weight: 700; color: var(--brand-slate);
  }

  /* back */
  .brand-band {
    position: absolute; left: 0; top: 0;
    width: 100%; height: 178px; background: var(--brand-red);
    display: flex; align-items: center; justify-content: center; gap: 18px;
  }
  .brand-band__circle {
    width: 62px; height: 62px; border-radius: 50%; background: var(--paper);
  }
  .brand-band__name {
    font-size: 54px; font-weight: 700; color: var(--paper); letter-spacing: -1px;
  }
  .credentials {
    position: absolute; left: 0; top: 232px; width: 100%;
    text-align: center; font-size: 13.5px; line-height: 18px; color: var(--ink);
  }
  .divisions {
    position: absolute; left: 0; top: 316px; width: 100%;
    display: flex; justify-content: center; gap: 30px; list-style: none;
  }
  .division {
    display: flex; align-items: center; gap: 6px;
    font-size: 15px; font-weight: 700; color: var(--brand-slate);
  }
  .division__square {
    width: 14px; height: 14px; background: var(--brand-slate);
  }
</style>
</head>
<body>
<main class="stage">
  <section class="card card--front" aria-label="Business card front">
    <div class="front-mark">
      <span class="front-mark__circle"></span>
      <span class="front-mark__name">tallowgatedeals</span>
    </div>
    <div class="accent-bar"></div>
    <h1 class="holder-name">Your Name</h1>
    <p class="holder-title">Title</p>
    <ul class="contact">
      <li class="contact__item">1300.418.572</li>
      <li class="contact__item">hello@tallowgatedeals.com.au</li>
      <li class="contact__item">www.tallowgatedeals.com.au</li>
      <li class="contact__item contact__item--address">Level 12, Kestrel House, 88 Marlow Street, Sydney NSW 2000</li>
    </ul>
  </section>

  <section class="card card--back" aria-label="Business card back">
    <div class="brand-band">
      <span class="brand-band__circle"></span>
      <span class="brand-band__name">tallowgatedeals</span>
    </div>
    <p class="credentials">
      Licensed Business Broker and Real Estate Agent Lic No. 30117264, Buyers Agent,<br>
      Member of Federation of Enterprise Brokers (FEB)
    </p>
    <ul class="divisions">
      <li class="division"><span class="division__square"></span>harrowlinkagent</li>
      <li class="division"><span class="division__square"></span>bramblegroceragent</li>
      <li class="division"><span class="division__square"></span>pinecrestfuelagent</li>
    </ul>
  </section>
</main>
</body>
</html>
```